Business card for Mortgage broker business

I have already had the logo designed and am needing a great looking business card. My business focus is on servicing clients who may not be able to obtain finance through traditional lenders due to bad credit, short term employment or they just don't fit the banks profile. It needs to be professional, trust worthy but also have a caring fell about it.
I have provided files showing the green and black logo, the white logo(on white background so the file looks blank) and also a file with the white logo with a background of leaves that was made up which will probably be used for a website header.

Industry/Entity Type

Finance

Contact Information for Business Card

Marcus Dalby
Managing Director, Accredited Finance Broker(AFB)
Po Box 817, Pakenham VIC 3810
marcus@kestrelfunding.com.au
www.kestrelfunding.com.au
0438 216 507

Requirements
Nice to have
• I have added a picture of myself as I would like to see some designs with the pic in it, but I'm not sure if I want it on there with the logo's or just the logo's

```html
<!DOCTYPE html>
<html lang="en">
<head>
<meta charset="utf-8">
<title>Business Card – Front and Back</title>
<link rel="stylesheet" href="https://fonts.googleapis.com/css2?family=Josefin+Sans:wght@300;400&family=Cormorant+Garamond:wght@500&display=swap">
<style>
  :root {
    --page-bg: #d8d5d0;
    --card-bg: #3a3836;
    --card-bg-edge: #333130;
    --ink-light: #ecebe8;
    --ink-soft: #cfcdc9;
    --ornament-tone: #bdbab5;
  }
  * { margin: 0; padding: 0; box-sizing: border-box; }
  html, body {
    width: 1200px;
    height: 960px;
    overflow: hidden;
    background: var(--page-bg);
  }
  .stage {
    position: relative;
    width: 1200px;
    height: 960px;
  }
  .card {
    position: absolute;
    left: 250px;
    width: 700px;
    height: 400px;
    background: radial-gradient(ellipse at 40% 30%, var(--card-bg) 0%, var(--card-bg-edge) 100%);
    box-shadow: 0 6px 18px rgba(0,0,0,0.18);
    color: var(--ink-light);
    font-family: "Josefin Sans", sans-serif;
    font-weight: 300;
  }
  .card--front { top: 50px; }
  .card--back  { top: 510px; }

  .rules {
    position: absolute;
    inset: 0;
    width: 700px;
    height: 400px;
  }
  .rules line { stroke: var(--ink-light); stroke-width: 1.6; }
  .rules circle { fill: var(--ink-light); }

  .person-name {
    position: absolute;
    left: 200px;
    top: 94px;
    font-size: 40px;
    font-weight: 400;
    letter-spacing: 2px;
    line-height: 1;
    white-space: nowrap;
  }
  .person-role {
    position: absolute;
    left: 202px;
    top: 142px;
    font-size: 12px;
    letter-spacing: 1px;
    color: var(--ink-soft);
    white-space: nowrap;
  }
  .ornament {
    position: absolute;
    width: 60px;
    height: 14px;
    border-radius: 7px;
    background: linear-gradient(90deg, transparent, var(--ornament-tone), transparent);
    opacity: 0.75;
  }
  .ornament--left  { left: 126px; top: 140px; }
  .ornament--right { left: 470px; top: 66px; }

  .contact {
    position: absolute;
    font-size: 17px;
    letter-spacing: 0.5px;
    white-space: nowrap;
  }
  .contact--phone { right: 385px; text-align: right; }
  .contact--phone-1 { top: 208px; }
  .contact--phone-2 { top: 246px; }
  .contact--email { left: 360px; top: 193px; }
  .contact--web   { left: 360px; top: 229px; }

  .address {
    position: absolute;
    left: 40px;
    top: 336px;
    font-size: 17px;
    letter-spacing: 1.5px;
    text-transform: uppercase;
    white-space: nowrap;
  }

  .brand-name {
    position: absolute;
    left: 0;
    right: 0;
    top: 180px;
    text-align: center;
    font-family: "Cormorant Garamond", serif;
    font-weight: 500;
    font-size: 34px;
    letter-spacing: 10px;
    text-transform: uppercase;
    color: var(--ink-light);
  }
</style>
</head>
<body>
<main class="stage">

  <section class="card card--front" aria-label="Business card front">
    <svg class="rules" viewBox="0 0 700 400" aria-hidden="true">
      <line x1="340" y1="188" x2="340" y2="322"/>
      <circle cx="340" cy="186" r="2.5"/>
      <circle cx="340" cy="324" r="2.5"/>
      <line x1="180" y1="234" x2="325" y2="234"/>
      <line x1="130" y1="272" x2="325" y2="272"/>
      <line x1="30" y1="302" x2="325" y2="302"/>
      <circle cx="28" cy="302" r="2.5"/>
      <line x1="355" y1="219" x2="640" y2="219"/>
      <circle cx="642" cy="219" r="2.5"/>
      <line x1="355" y1="255" x2="640" y2="255"/>
    </svg>

    <div class="ornament ornament--right" role="img" aria-label="Decorative scroll flourish"></div>
    <h1 class="person-name">MARCUS DALBY</h1>
    <p class="person-role">MANAGING DIRECTOR, ACCREDITED FINANCE BROKER (AFB)</p>
    <div class="ornament ornament--left" role="img" aria-label="Decorative scroll flourish"></div>

    <p class="contact contact--phone contact--phone-1">0438 216 507</p>
    <p class="contact contact--phone contact--phone-2">0438 216 507</p>
    <p class="contact contact--email">marcus@kestrelfunding.com.au</p>
    <p class="contact contact--web">www.kestrelfunding.com.au</p>

    <p class="address">Po Box 817, Pakenham VIC 3810</p>
  </section>

  <section class="card card--back" aria-label="Business card back">
    <p class="brand-name">Kestrel Funding</p>
  </section>

</main>
</body>
</html>
```